Pharmacy ad

need 2 pharmacy ads for the phone book. one for Birchfield Pharmacy and one for Corvane Rx Pharmacy. Dimensions for ad is 4.75in x 4.667 in. please see attached examples of ad uploaded as well logos of each pharmacy

```html
<!DOCTYPE html>
<html lang="en">
<head>
<meta charset="utf-8">
<title>Corvane Rx Pharmacy – Directory Ad</title>
<link rel="stylesheet" href="https://fonts.googleapis.com/css2?family=Mulish:wght@300;500;600;700;800;900&display=swap">
<style>
  :root {
    --brand-blue: #3f4a9a;
    --brand-green: #7ab929;
    --alert-red: #e2001a;
    --ink: #1c1c1c;
    --ink-soft: #3a3b52;
    --rule-grey: #b9b9bb;
    --panel: #f3f3f3;
    --paper: #ffffff;
  }
  * { box-sizing: border-box; margin: 0; padding: 0; }
  html, body { width: 1200px; height: 1179px; overflow: hidden; background: var(--paper); }
  body { font-family: "Mulish", sans-serif; color: var(--ink); }

  .ad { position: relative; width: 1200px; height: 1179px; border: 1px solid #c8c8d0; overflow: hidden; }

  /* Payment strip */
  .payments { position: absolute; left: 0; top: 0; width: 100%; height: 92px; background: var(--paper);
    border-bottom: 5px solid var(--rule-grey); }
  .payments__label { position: absolute; left: 188px; top: 26px; font-weight: 800; font-size: 36px;
    color: var(--brand-blue); font-variant: small-caps; letter-spacing: 0.5px; }
  .payments__arrow { position: absolute; left: 400px; top: 24px; }
  .payments__name { position: absolute; top: 32px; font-weight: 700; font-size: 22px; color: var(--brand-blue); }

  /* Hero */
  .hero { position: absolute; left: 0; top: 97px; width: 100%; height: 293px; background: var(--paper); }
  .brand { position: absolute; left: 62px; top: 118px; display: flex; align-items: center; gap: 22px; }
  .brand__square { width: 56px; height: 56px; background: var(--brand-blue); }
  .brand__name { font-weight: 800; font-size: 50px; color: var(--brand-blue); letter-spacing: -0.5px; }
  .tagline { position: absolute; left: 0; top: 0; }
  .tagline__word { position: absolute; left: 808px; font-weight: 800; font-size: 48px; color: var(--paper); }

  .divider { position: absolute; left: 0; width: 100%; height: 6px; background: var(--rule-grey); }

  /* Features */
  .store-visual { position: absolute; left: 0; top: 396px; width: 524px; height: 526px;
    background: linear-gradient(160deg, #e9ecef 0%, #d5dadf 45%, #b8bec4 100%); }
  .features { position: absolute; left: 524px; top: 396px; width: 676px; height: 526px; background: var(--panel); }
  .perk { position: absolute; left: 22px; display: flex; align-items: flex-start; gap: 22px; }
  .perk__box { flex: none; margin-top: 2px; }
  .perk__title { font-weight: 500; font-size: 32px; line-height: 1; }
  .perk__note { font-weight: 300; font-size: 22px; margin-top: 8px; }
  .certified { position: absolute; left: 78px; top: 204px; font-weight: 900; font-size: 37px; color: var(--alert-red); }
  .services { position: absolute; left: 34px; top: 268px; list-style: none; }
  .services li { position: relative; padding-left: 44px; font-weight: 500; font-size: 31.5px; line-height: 38.6px; }
  .services li::before { content: ""; position: absolute; left: 0; top: 19px; width: 12px; height: 4px; background: var(--brand-blue); }

  /* Delivery band */
  .delivery { position: absolute; left: 0; top: 926px; width: 100%; height: 116px; background: var(--brand-blue); color: var(--paper); }
  .delivery__title { position: absolute; left: 56px; top: 30px; font-weight: 900; font-size: 48px; }
  .delivery__hours { position: absolute; left: 554px; top: 24px; font-weight: 800; font-size: 29px; line-height: 36px; }

  /* Footer */
  .contact { position: absolute; left: 0; top: 1048px; width: 100%; height: 131px; background: var(--panel); }
  .contact__icon { position: absolute; left: 94px; }
  .contact__text { position: absolute; left: 158px; top: 14px; font-weight: 700; font-size: 29px; line-height: 34px; color: var(--ink-soft); }
  .contact__rule { position: absolute; left: 663px; top: 20px; width: 3px; height: 88px; background: var(--brand-blue); }
  .social { position: absolute; left: 740px; top: 24px; display: flex; align-items: center; gap: 24px; }
  .social__text { font-weight: 700; font-size: 31px; line-height: 38px; color: var(--ink-soft); text-align: right; }
  .social__square { width: 80px; height: 80px; border-radius: 6px; background: var(--brand-blue); }
</style>
</head>
<body>
<div class="ad">

  <header class="payments">
    <div class="payments__label">We Accept</div>
    <svg class="payments__arrow" width="42" height="52" viewBox="0 0 42 52" aria-hidden="true">
      <polygon points="2,0 16,0 42,26 16,52 2,52 28,26" fill="var(--brand-blue)"/>
    </svg>
    <span class="payments__name" style="left:470px">Paycrest</span>
    <span class="payments__name" style="left:570px">Cardwell</span>
    <span class="payments__name" style="left:672px">Solvane</span>
    <span class="payments__name" style="left:764px">Harbora Insurances</span>
  </header>

  <section class="hero">
    <div class="brand">
      <div class="brand__square"></div>
      <div class="brand__name">Corvane Rx Pharmacy</div>
    </div>
    <svg class="tagline" width="1200" height="293" viewBox="0 0 1200 293" aria-hidden="true">
      <polygon points="772,0 1200,0 1200,100 712,100" fill="var(--brand-blue)"/>
      <polygon points="710,104 1200,104 1200,182 710,182 684,143" fill="var(--brand-green)"/>
      <polygon points="710,186 1200,186 1200,293 776,293" fill="var(--brand-blue)"/>
    </svg>
    <div class="tagline__word" style="top:22px">Where</div>
    <div class="tagline__word" style="top:103px">Good Health</div>
    <div class="tagline__word" style="top:187px">Begins</div>
  </section>

  <div class="divider" style="top:390px"></div>

  <div class="store-visual" role="img" aria-label="Photo of a bright pharmacy aisle with white shelves stocked with medicine boxes"></div>

  <section class="features">
    <div class="perk" style="top:40px">
      <svg class="perk__box" width="32" height="32" viewBox="0 0 32 32" aria-hidden="true">
        <rect x="2" y="4" width="26" height="26" fill="none" stroke="var(--brand-blue)" stroke-width="3.5"/>
        <path d="M8 16 L14 23 L30 3" fill="none" stroke="var(--alert-red)" stroke-width="4.5" stroke-linecap="round" stroke-linejoin="round"/>
      </svg>
      <div class="perk__title">10 % senior citizen discount</div>
    </div>
    <div class="perk" style="top:100px">
      <svg class="perk__box" width="32" height="32" viewBox="0 0 32 32" aria-hidden="true">
        <rect x="2" y="4" width="26" height="26" fill="none" stroke="var(--brand-blue)" stroke-width="3.5"/>
        <path d="M8 16 L14 23 L30 3" fill="none" stroke="var(--alert-red)" stroke-width="4.5" stroke-linecap="round" stroke-linejoin="round"/>
      </svg>
      <div>
        <div class="perk__title">10 % Student discount</div>
        <div class="perk__note">(With valid ID card)</div>
      </div>
    </div>

    <div class="certified">Certified Pharmacists</div>

    <ul class="services">
      <li>Affordable prices</li>
      <li>Brand and Generic Medicines</li>
      <li>Blood Pressure and Glucose checks</li>
      <li>Personal care and Beauty Products</li>
      <li>Injectables</li>
      <li>Special Orders</li>
    </ul>
  </section>

  <div class="divider" style="top:920px"></div>

  <section class="delivery">
    <div class="delivery__title">Delivery service :</div>
    <div class="delivery__hours">Monday – Saturday Thursday 8am- 7pm<br>Sunday 10am-2pm</div>
  </section>

  <div class="divider" style="top:1042px"></div>

  <footer class="contact">
    <svg class="contact__icon" style="top:16px" width="30" height="30" viewBox="0 0 30 30" aria-hidden="true">
      <polygon points="15,1 1,14 5,14 5,29 25,29 25,14 29,14" fill="var(--ink)"/>
      <rect x="12" y="18" width="6" height="6" fill="var(--panel)"/>
    </svg>
    <svg class="contact__icon" style="top:86px" width="28" height="28" viewBox="0 0 24 24" aria-hidden="true">
      <path d="M6.6 10.8a15.1 15.1 0 0 0 6.6 6.6l2.2-2.2c.3-.3.7-.4 1-.2 1.1.4 2.3.6 3.6.6.6 0 1 .4 1 1V20c0 .6-.4 1-1 1C10.6 21 3 13.4 3 4c0-.6.4-1 1-1h3.5c.6 0 1 .4 1 1 0 1.3.2 2.5.6 3.6.1.3 0 .7-.2 1z" fill="var(--ink)"/>
    </svg>
    <div class="contact__text">Unit B4, Marlow Court Hotel,<br>Shore Road, Fenwick<br>555-0142</div>
    <div class="contact__rule"></div>
    <div class="social">
      <div class="social__text">Visit us on<br>Connectly</div>
      <div class="social__square"></div>
    </div>
  </footer>

</div>
</body>
</html>
```